Kestrel Capital Circle - Paradigm Shifting Investment Vehicle in Bali*

The presentation is for the Kestrel Capital Circle, a future-thinking and paradigm-shifting leadership collective that is aimed at uniting conscious investors with New Earth projects in Bali, Indonesia. We want to create a presentation pitch deck to investors that encompasses that concept, pairing our royal purple logo with elements of natural green, or white/black that feels organic, purposeful and powerful. Example of our investor deck is attached.

Target Market(s)

High Net Worth Conscious Individuals, Wealthy Nomads looking to move to Bali, community building leaders

Industry/Entity Type

Investment

Logo Text

Kestrel Capital Circle

Font styles to use
Serif
Sans Serif

Colors
6b449b
886aae
b8a6cd
acd037
cadf82
add136
00a990
33b8a4
86cfc6

Requirements
Must have
• Our name of "Kestrel Capital Circle" or "KCC"
Nice to have
• keywords: consciousness, transformational, healing, new paradigm, progress, New Earth, abundance, regenerative, royal, natural, organic, sustainability, future, dream, creation, co-creation
Should not have
• Boring, corporate look

```html
<!DOCTYPE html>
<html lang="en">
<head>
<meta charset="utf-8">
<title>Kestrel Capital Circle – Investor Deck</title>
<link href="https://fonts.googleapis.com/css2?family=Playfair+Display+SC:wght@400;700&family=Lato:ital,wght@0,400;0,700;1,400&display=swap" rel="stylesheet">
<style>
:root{
  --page:#ffffff;
  --cream:#f7f6ee;
  --plum:#4b1e45;
  --plum-band:rgba(88,36,86,.55);
  --green:#1f5e4d;
  --teal:#2a9d86;
  --mint:#5fd0b6;
  --olive:#a4a873;
  --rose:#b07a72;
  --pink:#c99ac6;
  --magenta:#b35aa3;
  --ink:#2d4a40;
  --serif:'Playfair Display SC',Georgia,serif;
  --sans:'Lato',Arial,sans-serif;
}
*{box-sizing:border-box;margin:0;padding:0}
html,body{width:900px;height:1200px;overflow:hidden;background:var(--page)}
.deck{position:relative;width:900px;height:1200px}
.slide{position:absolute;width:312px;height:175px;background:var(--cream);overflow:hidden;box-shadow:4px 6px 10px rgba(0,0,0,.22);font-family:var(--sans);color:var(--ink)}
.col-l{left:105px}.col-r{left:472px}
.r1{top:22px}.r2{top:215px}.r3{top:408px}.r4{top:601px}.r5{top:794px}.r6{top:987px}
.abs{position:absolute}
.photo{position:absolute}
.band{position:absolute;top:0;right:11px;width:27px;height:100%;background:var(--plum-band)}
.band.solid{right:0;width:38px;background:var(--plum)}
.mark{position:absolute;display:flex;align-items:center;gap:2px;font-family:var(--serif);font-size:6px;color:var(--plum);letter-spacing:.5px}
.mark .sq{width:7px;height:7px;background:var(--plum)}
.mark.light{color:var(--cream)}
.mark.light .sq{background:var(--cream)}
.title{font-family:var(--serif);color:var(--plum);font-weight:400;line-height:1.1}
.body{font-size:4.3px;line-height:1.45;text-align:justify}
.body p+p{margin-top:4px}
.body b{color:var(--green)}
</style>
</head>
<body>
<div class="deck">

<!-- 1 Cover -->
<section class="slide col-l r1">
  <div class="photo" style="inset:0;background:linear-gradient(180deg,#8e8ea6 0%,#b7b3bf 30%,#5e6e6a 55%,#3f4a3c 70%,#6f8a86 85%,#52676a 100%)" role="img" aria-label="Lakeside temple pagoda under misty clouds with flower gardens"></div>
  <div class="band"></div>
  <div class="mark light" style="top:30px;right:13px"><span class="sq"></span>KCC</div>
  <h1 class="title abs" style="right:43px;top:32px;font-size:12px;color:var(--plum);text-align:right">Kestrel Capital Circle</h1>
  <p class="abs" style="right:43px;top:52px;font-family:var(--serif);font-size:4.5px;color:var(--plum)">Invest in Bali | Live in Paradise | Join the Club</p>
  <p class="abs" style="right:48px;top:62px;font-family:var(--serif);font-size:3.8px;letter-spacing:1.2px;color:var(--plum)">Investment Prospectus | August 2020</p>
</section>

<!-- 2 Welcome -->
<section class="slide col-r r1">
  <div class="photo" style="inset:0;background:linear-gradient(180deg,#d7836a 0%,#f2a97a 25%,#e9b48e 45%,#c88579 62%,#8f6a7c 75%,#6d5a72 100%)" role="img" aria-label="Glowing orange sunset clouds over a calm sea"></div>
  <div class="band"></div>
  <div class="mark light" style="top:30px;right:13px"><span class="sq"></span>KCC</div>
  <h1 class="title abs" style="right:52px;top:28px;font-size:21px;text-align:right">Welcome</h1>
  <h1 class="title abs" style="right:42px;top:55px;font-size:21px;text-align:right">KCC Overview</h1>
</section>

<!-- 3 The world is changing -->
<section class="slide col-l r2">
  <h2 class="title abs" style="left:25px;top:38px;font-size:13px"><span style="color:var(--rose)">The World</span><br>is Changing</h2>
  <p class="body abs" style="left:25px;top:80px;width:135px;font-size:5.6px;line-height:1.35">“The world is undergoing a great transformational change; new ideas, beliefs, and concepts are required for humanity to shift to the next stage of evolution, with a focus on shared values of planetary sustainability, business integrity, and loving compassion for all living things.”</p>
  <p class="abs" style="right:150px;top:143px;font-family:var(--serif);font-size:5.5px;color:var(--plum)">Kestrel Capital Circle</p>
  <div class="photo" style="left:169px;top:0;width:105px;height:175px;background:linear-gradient(180deg,#eadfd4 0%,#cdbfae 35%,#6a6d54 52%,#b9ad9e 70%,#8d8272 100%)" role="img" aria-label="Temple pagoda reflected in a still misty lake"></div>
  <div class="band solid"></div>
  <div class="mark light" style="top:40px;right:9px"><span class="sq"></span>KCC</div>
</section>

<!-- 4 What is KCC -->
<section class="slide col-r r2">
  <svg class="abs" style="left:130px;top:108px" width="60" height="70" viewBox="0 0 60 70"><path d="M0 70 C4 30 30 5 60 0 L60 70 Z" fill="var(--olive)"/></svg>
  <div class="mark" style="left:13px;top:14px"><span class="sq"></span>KCC</div>
  <h2 class="title abs" style="right:165px;top:42px;font-size:13.5px;text-align:right;white-space:nowrap">What is Kestrel<br>Capital Circle?</h2>
  <div class="body abs" style="left:16px;top:80px;width:131px;font-size:4.9px">
    <p><b>Kestrel Capital Circle (KCC)</b> is a social club of conscious investors, influencers and entrepreneurs creating the New Paradigm.</p>
    <p>Our mission is to support profitable impact-driven projects, improve the lives of our members and the local community, and foster greater sustainability on the island of Bali.</p>
  </div>
  <div class="photo" style="left:166px;top:0;width:117px;height:175px;background:linear-gradient(180deg,#3a2b2a 0%,#c7733a 18%,#b9a3c0 40%,#e5a98e 55%,#7a6c6a 72%,#4d5a34 100%)" role="img" aria-label="Woven lanterns above a beach with umbrellas at sunset"></div>
</section>

<!-- 5 New paradigm -->
<section class="slide col-l r3">
  <div class="photo" style="left:26px;top:34px;width:111px;height:141px;background:linear-gradient(160deg,#3f5a2e 0%,#8d8c70 40%,#b5b094 60%,#55653d 100%)" role="img" aria-label="Stone statue of a seated figure among tropical foliage"></div>
  <div class="mark" style="right:14px;top:14px"><span class="sq"></span>KCC</div>
  <h2 class="title abs" style="left:151px;top:28px;font-size:13.5px;color:var(--green)">The New<br>Paradigm</h2>
  <div class="body abs" style="left:151px;top:70px;width:132px">
    <p>A <b>paradigm</b> is generally defined as a framework that has unwritten rules and that directs actions. A <b>shift</b> occurs when one <b>paradigm</b> loses its influence and another takes over. We are witnessing the collapse of the old paradigm; a system built on scarcity, lack, and fear. Hence, we sit on the precipice of a <b>New Paradigm</b> – a loving, supportive, and collaborative framework that provides abundance for everyone.</p>
    <p>Bali is the epicenter for emerging ideas; it is a hub for new networks, systems, communities, and projects that redefine the way we relate to each other and the world.</p>
  </div>
</section>

<!-- 6 Core values -->
<section class="slide col-r r3">
  <svg class="abs" style="left:4px;top:0" width="282" height="125" viewBox="0 0 282 125" role="img" aria-label="Water palace garden with stepping stones, fountains and a stone guardian statue">
    <defs><linearGradient id="water" x1="0" y1="0" x2="0" y2="1"><stop offset="0" stop-color="#cfe0e4"/><stop offset=".4" stop-color="#5d7a45"/><stop offset=".7" stop-color="#6f8a88"/><stop offset="1" stop-color="#4d6868"/></linearGradient></defs>
    <path d="M0 0 H282 C262 50 210 110 130 122 C70 130 20 110 0 40 Z" fill="url(#water)"/>
  </svg>
  <div class="mark light" style="left:14px;top:14px"><span class="sq"></span>KCC</div>
  <h2 class="title abs" style="right:19px;top:73px;font-size:13px;color:var(--green);text-align:right">Our<br>Core Values</h2>
  <p class="abs" style="left:205px;top:111px;font-family:var(--serif);font-size:5.5px;color:var(--plum);font-weight:700">· &nbsp;People. Planet. Profit.</p>
  <p class="abs" style="left:205px;top:125px;font-family:var(--serif);font-size:5.5px;color:var(--plum);font-weight:700">· &nbsp;Truth. Trust. Faith.</p>
  <p class="body abs" style="left:14px;top:139px;width:287px;font-size:4.9px">KCC invests in initiatives that are beneficial for the people, the planet, and profits; this means that every stakeholder is considered. Stakeholders are its members, partners, employees, and the planet. Impact is what drives our members, while profits are what sustains them.</p>
</section>

<!-- 7 Why Bali -->
<section class="slide col-l r4">
  <div class="abs" style="left:0;top:0;width:205px;height:175px;background:linear-gradient(120deg,#efe6d6 0%,#f3ede2 45%,var(--cream) 70%)" role="img" aria-label="Soft beige diagonal stripe pattern"></div>
  <div class="mark" style="right:14px;top:14px"><span class="sq"></span>KCC</div>
  <h2 class="title abs" style="left:17px;top:18px;font-size:13px;color:var(--green)">Why Bali?</h2>
  <p class="abs" style="left:17px;top:42px;font-size:6.3px;color:var(--ink)">Asked from a different perspective, <b>WHY NOT</b> Bali?</p>
  <div class="body abs" style="left:17px;top:56px;width:175px;font-size:5.2px;line-height:1.33;text-align:left">
    <p>Bali offers Western country nationals an extremely low cost of living and an amazing quality of life. For example, Canggu is rated as a top 5 digital nomad destination in the world. Benefits of living on the “Island of the Gods” include affordability, friendly locals, low crime, great weather, and access to nature and healthy living. A number of expats have moved to Bali to experience life in paradise in recent years.</p>
    <p>Moreover, with increased border control and immigration restrictions resulting from COVID-19, as well as the challenging impact that the virus has had on the lifestyle of people in Western countries, gaining a work and residency permit for Bali has become more desirable. There has been little impact from COVID-19 in Bali compared to other geographies, which makes it even more attractive as a destination.</p>
  </div>
  <svg class="abs" style="left:195px;top:44px" width="117" height="131" viewBox="0 0 117 131" role="img" aria-label="Volcano rising above green rice terraces under a pink dusk sky">
    <defs><linearGradient id="terr" x1="0" y1="0" x2="0" y2="1"><stop offset="0" stop-color="#b4578f"/><stop offset=".3" stop-color="#e48ba0"/><stop offset=".5" stop-color="#5f4a7a"/><stop offset=".75" stop-color="#4f7a3a"/><stop offset="1" stop-color="#82a64a"/></linearGradient></defs>
    <path d="M117 0 H60 C15 10 0 50 3 85 C6 110 15 125 25 131 H117 Z" fill="url(#terr)"/>
  </svg>
</section>

<!-- 8 KITAS -->
<section class="slide col-r r4">
  <div class="photo" style="left:0;top:0;width:60px;height:175px;background:linear-gradient(90deg,#2f4a25 0%,#5d7a45 40%,#a8b39c 55%,#3d5a2c 100%)" role="img" aria-label="Tall jungle waterfall"></div>
  <div class="mark" style="right:14px;top:16px"><span class="sq"></span>KCC</div>
  <h2 class="title abs" style="left:73px;top:18px;font-size:13px;color:var(--green)">What is a KITAS?</h2>
  <div class="body abs" style="left:73px;top:47px;width:222px;font-size:4.3px">
    <p>A <b>KITAS (<i>Kartu Izin Tinggal Sementara</i>, or Temporary Stay Permit Card)</b> is an Indonesian government permit that allows foreign nationals to stay for a specified period of time without having to renew their visas and/or work in Indonesia. When border restrictions are enforced, it is the only way for a foreigner to enter the country.</p>
    <p style="font-size:3.9px">There are <b>two</b> ways to obtain a KITAS:<br>&nbsp;1. &nbsp;Company Sponsorship: an existing business in Bali employs and sponsors a person<br>&nbsp;2. &nbsp;Investor KITAS: invest $175,000+ into a foreign-owned local entity (PT PMA) and receive an Investor KITAS for two years, with the option to extend</p>
    <p style="font-weight:700;color:var(--green)">The Kestrel Capital Circle offers an alternative.</p>
    <p>Among other benefits mentioned previously, the KCC membership will include a 2-year commissioner KITAS, with the option to extend. While this option does require a capital investment, it is considerably less than USD $175,000 and requires zero knowledge, experience and motivation to manage a business in Bali; supports local people and the land; provides a potential return on Investment; and gives positive ROI on impact driven investments.</p>
  </div>
</section>

<!-- 9 Becoming a member cover -->
<section class="slide col-l r5">
  <div class="photo" style="inset:0;background:linear-gradient(180deg,#2c6f9e 0%,#9cc3d8 25%,#5c6a3c 38%,#2a9fb8 55%,#41c6d1 70%,#e4f1f2 100%)" role="img" aria-label="Turquoise waves crashing below a jungle-covered cliff"></div>
  <div class="band"></div>
  <div class="mark light" style="top:30px;right:13px"><span class="sq"></span>KCC</div>
  <h1 class="title abs" style="right:52px;top:22px;font-size:25px;color:#f4f1ec;text-align:right;line-height:1.25">Becoming<br>a Member</h1>
</section>

<!-- 10 Steps -->
<section class="slide col-r r5">
  <div class="mark" style="right:14px;top:15px"><span class="sq"></span>KCC</div>
  <h2 class="title abs" style="left:22px;top:20px;font-size:13px">Becoming a Member</h2>
  <p class="abs" style="left:27px;top:52px;width:258px;font-size:4.3px;line-height:1.4;color:var(--plum)">KCC invites a limited number of members to join the club each month, and is selective based on a number of factors. There is a USD $1,000 deposit which is refunded to unsuccessful applicants. Remainder payment of USD $24,000* must be made within 48 hours of approval.</p>
  <svg class="abs" style="left:0;top:0" width="312" height="175" viewBox="0 0 312 175" font-family="Lato, Arial, sans-serif">
    <rect x="30" y="107" width="80" height="4" fill="#184a3c"/>
    <rect x="110" y="107" width="80" height="4" fill="var(--teal)"/>
    <rect x="190" y="107" width="40" height="4" fill="var(--pink)"/>
    <rect x="230" y="107" width="38" height="4" fill="var(--plum)"/>
    <g fill="var(--plum)" font-size="3.4" font-weight="700">
      <text x="29" y="88">Submit Application and</text><text x="29" y="92">$1,000 Deposit</text>
      <text x="109" y="88">Receive Invitation to Join</text>
      <text x="189" y="88">Receive Membership ID</text><text x="189" y="92">&amp; Legal Documents</text>
      <text x="262" y="88">Open Club</text><text x="262" y="92">Bank Account</text>
      <text x="69" y="124">Interview with KCC</text><text x="69" y="128">Founder</text>
      <text x="149" y="124">Sign Membership</text><text x="149" y="128">Agreement &amp; Make</text><text x="149" y="132">Balance Payment</text>
      <text x="227" y="124">Begin KITAS</text><text x="227" y="128">Processing</text>
    </g>
    <g fill="#8a7a88" font-size="3.2">
      <text x="149" y="140">Must be completed within</text><text x="149" y="144">48 hours of approval</text>
      <text x="227" y="138">This process may</text><text x="227" y="142">take up to 2-3</text><text x="227" y="146">months to</text><text x="227" y="150">complete</text>
    </g>
    <g stroke="#999" stroke-width=".4">
      <line x1="30" y1="98" x2="30" y2="107"/><line x1="110" y1="98" x2="110" y2="107"/><line x1="190" y1="98" x2="190" y2="107"/><line x1="268" y1="98" x2="268" y2="107"/>
      <line x1="70" y1="111" x2="70" y2="119"/><line x1="150" y1="111" x2="150" y2="119"/><line x1="228" y1="111" x2="228" y2="119"/>
    </g>
    <g fill="var(--plum)"><circle cx="30" cy="98" r="1.2"/><circle cx="268" cy="98" r="1.2"/><circle cx="228" cy="119" r="1.2"/></g>
    <g fill="var(--green)"><circle cx="70" cy="119" r="1.2"/></g>
    <g fill="var(--teal)"><circle cx="110" cy="98" r="1.2"/></g>
    <g fill="var(--pink)"><circle cx="190" cy="98" r="1.2"/><circle cx="150" cy="119" r="1.2"/></g>
    <g fill="var(--plum)" font-size="6" font-weight="700">
      <text x="62" y="104">Step 2</text><text x="142" y="104">Step 4</text><text x="222" y="104">Step 6</text>
      <text x="22" y="118">Step 1</text><text x="102" y="118">Step 3</text><text x="182" y="118">Step 5</text><text x="259" y="118">Step 7</text>
    </g>
    <text x="72" y="166" font-size="2.6" font-style="italic" fill="#8a7a88">*$29,000 membership fee may be a tax-deductible gift for eligible donors. $5,000 discount for current KITAS holders</text>
  </svg>
</section>

<!-- 11 Member benefits -->
<section class="slide col-l r6">
  <div class="mark" style="right:14px;top:15px"><span class="sq"></span>KCC</div>
  <h2 class="title abs" style="left:21px;top:20px;font-size:13px">Member Benefits</h2>
  <svg class="abs" style="left:0;top:0" width="312" height="175" viewBox="0 0 312 175" font-family="Lato, Arial, sans-serif">
    <rect x="19" y="44" width="276" height="25" fill="var(--green)"/>
    <text x="42" y="58.5" font-family="Playfair Display SC, Georgia, serif" font-size="4.6" letter-spacing="1" fill="#fff">EXAMPLE BASED ON USD $25,000 INVESTMENT</text>
    <g font-family="Playfair Display SC, Georgia, serif" font-size="3" fill="#fff" text-anchor="middle">
      <text x="233" y="53">OPTION A</text><text x="233" y="57">INVESTMENT CLUB</text><text x="233" y="61" font-style="italic">( EG. VCEI PROJECT)</text>
      <text x="276" y="56">OPTION B</text><text x="276" y="60">BUSINESS CLUB</text>
    </g>
    <g font-size="3.9" fill="var(--plum)">
      <text x="21" y="76" font-style="italic">100 shares in (VCEI) PT Verdant Clove Estates Indonesia (ROI $115,106)*</text>
      <text x="21" y="85" font-style="italic">Proceeds from the sales of product from a personal vanilla farm with 500 plants (ROI $56,687)*</text>
      <text x="21" y="94">USD $10,000 in a bank account for investment into existing or new project</text>
      <text x="21" y="102">A two-year KITAS work visa, with the option to extend</text>
      <text x="21" y="110">Access to exclusive networking events and investment opportunities</text>
      <text x="21" y="118">First right of refusal on new investment opportunities</text>
      <text x="21" y="126">Access to professional business services; finance, legal, accounting and tax advice to</text>
      <text x="21" y="130.5">minimise tax and maximise returns.</text>
      <text x="21" y="139">Access to support for migration: travel, accommodation and recommendations (restaurants,</text>
      <text x="21" y="143.5">activities, wellness facilities, etc.)</text>
      <text x="21" y="152">Opportunity to become a founding member and earn 6 figures</text>
    </g>
    <g font-size="4" fill="#8a8a7a" text-anchor="middle">
      <text x="233" y="76">✓</text><text x="233" y="85">✓</text><text x="276" y="94">✓</text>
      <text x="233" y="102">✓</text><text x="276" y="102">✓</text><text x="233" y="110">✓</text><text x="276" y="110">✓</text>
      <text x="233" y="118">✓</text><text x="276" y="118">✓</text><text x="233" y="128">✓</text><text x="276" y="128">✓</text>
      <text x="233" y="141">✓</text><text x="276" y="141">✓</text><text x="233" y="152">✓</text><text x="276" y="152">✓</text>
    </g>
    <text x="21" y="165" font-size="2.6" font-style="italic" fill="var(--plum)">*Projected over 15 years</text>
  </svg>
</section>

<!-- 12 Fee breakdown -->
<section class="slide col-r r6">
  <div class="mark" style="right:14px;top:15px"><span class="sq"></span>KCC</div>
  <h2 class="title abs" style="left:21px;top:20px;font-size:13px">Membership Fee Breakdown</h2>
  <div class="abs" style="left:21px;top:47px;width:150px;font-size:4.6px;line-height:1.5;color:var(--plum)">
    <p style="margin-bottom:2px">Based on a USD $25,000 investment, we allocate the following:</p>
    <p style="padding-left:5px"><b>› &nbsp;Personal KCC Business Account (USD $10,000):</b></p>
    <p style="padding-left:14px">◦ Freedom of making investments within KCC ventures portfolio and/or individual business activities</p>
    <p style="padding-left:5px"><b>› &nbsp;Club Costs (USD $8,250):</b></p>
    <p style="padding-left:14px">◦ Operations, membership services, KITAS</p>
    <p style="padding-left:5px"><b>› &nbsp;Programs (USD $3,000):</b></p>
    <p style="padding-left:14px">◦ Vocational and charitable assistance programs to aid the local Balinese communities</p>
    <p style="padding-left:5px"><b>› &nbsp;Club Investment Capital (USD $2,500):</b></p>
    <p style="padding-left:14px">◦ Capital for Founding Members to invest</p>
    <p style="padding-left:5px"><b>› &nbsp;Club Cash Reserves (USD $1,250):</b></p>
    <p style="padding-left:14px">◦ Cash flow is king. The club keeps cash on reserve for miscellaneous expenses</p>
  </div>
  <p class="abs" style="left:21px;top:163px;font-size:2.6px;font-style:italic;color:var(--plum)">*$5,000 discount for KITAS holders</p>
  <svg class="abs" style="left:180px;top:44px" width="104" height="128" viewBox="0 0 104 128" font-family="Lato, Arial, sans-serif">
    <g transform="rotate(-90 52 50)" fill="none" stroke-width="9">
      <circle cx="52" cy="50" r="42" pathLength="100" stroke="var(--teal)" stroke-dasharray="40 60" stroke-dashoffset="0"/>
      <circle cx="52" cy="50" r="42" pathLength="100" stroke="#184a3c" stroke-dasharray="5 95" stroke-dashoffset="-40"/>
      <circle cx="52" cy="50" r="42" pathLength="100" stroke="var(--plum)" stroke-dasharray="33 67" stroke-dashoffset="-45"/>
      <circle cx="52" cy="50" r="42" pathLength="100" stroke="var(--magenta)" stroke-dasharray="6 94" stroke-dashoffset="-78"/>
      <circle cx="52" cy="50" r="42" pathLength="100" stroke="var(--pink)" stroke-dasharray="10 90" stroke-dashoffset="-84"/>
      <circle cx="52" cy="50" r="42" pathLength="100" stroke="var(--mint)" stroke-dasharray="6 94" stroke-dashoffset="-94"/>
    </g>
    <g font-size="3.2" fill="var(--plum)">
      <rect x="2" y="104" width="2" height="2" fill="var(--teal)"/><text x="6" y="106">Investment</text>
      <rect x="2" y="110" width="2" height="2" fill="var(--plum)"/><text x="6" y="112">Administrative Expenses</text>
      <rect x="2" y="116" width="2" height="2" fill="var(--pink)"/><text x="6" y="118">CIC</text>
      <rect x="64" y="104" width="2" height="2" fill="#184a3c"/><text x="68" y="106">Charity</text>
      <rect x="64" y="110" width="2" height="2" fill="var(--magenta)"/><text x="68" y="112">Vocation Program</text>
      <rect x="64" y="116" width="2" height="2" fill="var(--mint)"/><text x="68" y="118">Cash Reserves</text>
    </g>
  </svg>
</section>

</div>
</body>
</html>
```